ROV Wellcare Inc. Business Card and Stationery
Business Logo  - Health
Business Logo
Professional
Teresa Okonkwo
Registered Office: 14 S Pebblecroft Ln Schaumburg IL 60195 Phone: 847-555-0182 WareHouse Address: 2417 Bellhaven Street Schaumburg IL 60174 Phone: 847-555-0147
teresa@rovwellcare.example
www.rovwellcare.example

```html
<!DOCTYPE html>
<html lang="en">
<head>
<meta charset="utf-8">
<title>Larkspur Medical Group Stationery</title>
<link href="https://fonts.googleapis.com/css2?family=Open+Sans:wght@400;600;700&display=swap" rel="stylesheet">
<style>
:root{
  --bg:#2b2b2b;
  --paper:#ffffff;
  --green:#7cc225;
  --blue:#2368b3;
  --ink:#2a3a4a;
  --muted:#8a96a0;
  --label:#9aa3aa;
  --faint:#e6eef5;
  --line:#cfd6dc;
  --field:#9aa4ac;
}
*{margin:0;padding:0;box-sizing:border-box}
html,body{width:1200px;height:379px;overflow:hidden;background:var(--bg);font-family:"Open Sans",Arial,sans-serif}
.canvas{position:relative;width:1200px;height:379px}
.piece{position:absolute;background:var(--paper);overflow:hidden;box-shadow:0 2px 6px rgba(0,0,0,.5)}
.label{position:absolute;color:var(--label);font-size:6px;text-align:center}
.brand{display:flex;align-items:center;gap:4px;color:var(--blue);font-weight:700;white-space:nowrap}
.brand .dot{border-radius:50%;background:var(--blue);flex:none}
.wave{position:absolute;left:0;bottom:0;width:100%}
.intro{position:absolute;left:12px;top:78px}
.intro .brand{font-size:12px;color:#fff}
.intro .brand .dot{width:22px;height:22px;background:var(--green)}
.intro p{color:#cfd6db;font-size:7px;margin-top:4px}
.card-info{position:absolute;font-size:4.5px;color:var(--ink);line-height:1.5;white-space:nowrap}
.card-info strong{font-size:6px;display:block;color:var(--blue)}
.card-info.on-green,.card-info.on-green strong{color:#fff}
.faint-mark{position:absolute;border-radius:50%;background:var(--faint)}
.form-table{position:absolute;left:14px;top:18px;width:176px;border-collapse:collapse}
.form-table td{border:1px solid var(--line);height:8px;font-size:4px;color:var(--muted);padding-left:2px}
.form-table td.fill{background:var(--field)}
.side-panel{position:absolute;right:0;top:0;bottom:0;width:46%;background:var(--green)}
</style>
</head>
<body>
<main class="canvas">

  <section class="intro">
    <div class="brand"><span class="dot"></span>Larkspur Medical Group</div>
    <p>Stationery Template</p>
  </section>

  <article class="piece" style="left:12px;top:161px;width:144px;height:72px">
    <div class="brand" style="position:absolute;left:8px;top:8px;font-size:7px"><span class="dot" style="width:12px;height:12px"></span>Larkspur Medical Group</div>
    <div class="card-info" style="left:40px;top:30px"><strong>Teresa Okonkwo</strong>teresa@larkspurmedical.example</div>
    <svg class="wave" viewBox="0 0 144 20" height="20" preserveAspectRatio="none"><path d="M0 10 Q72 -4 144 8 V20 H0Z" fill="var(--green)"/><path d="M0 12 Q72 0 144 10" stroke="var(--blue)" stroke-width="1.5" fill="none"/></svg>
  </article>
  <div class="label" style="left:12px;top:236px;width:144px">Business Card Front</div>

  <article class="piece" style="left:12px;top:247px;width:144px;height:72px">
    <div class="brand" style="position:absolute;left:8px;top:8px;font-size:7px"><span class="dot" style="width:12px;height:12px"></span>Larkspur Medical Group</div>
    <div class="card-info" style="left:40px;top:30px"><strong>Teresa Okonkwo</strong>www.larkspurmedical.example</div>
    <svg class="wave" viewBox="0 0 144 20" height="20" preserveAspectRatio="none"><path d="M0 10 Q72 -4 144 8 V20 H0Z" fill="var(--green)"/><path d="M0 12 Q72 0 144 10" stroke="var(--blue)" stroke-width="1.5" fill="none"/></svg>
  </article>
  <div class="label" style="left:12px;top:322px;width:144px">Business Card Back</div>

  <article class="piece" style="left:180px;top:24px;width:204px;height:318px">
    <div class="brand" style="position:absolute;left:12px;top:12px;font-size:7px"><span class="dot" style="width:12px;height:12px"></span>Larkspur Medical Group</div>
    <div class="faint-mark" style="left:42px;top:90px;width:120px;height:120px"></div>
    <svg class="wave" viewBox="0 0 204 30" height="30" preserveAspectRatio="none"><path d="M0 14 Q100 -2 204 12 V30 H0Z" fill="var(--green)"/><path d="M0 16 Q100 0 204 14" stroke="var(--blue)" stroke-width="2" fill="none"/></svg>
  </article>
  <div class="label" style="left:180px;top:346px;width:204px">Letterhead Page</div>

  <article class="piece" style="left:391px;top:24px;width:204px;height:318px">
    <table class="form-table">
      <tr><td>To</td><td class="fill"></td><td>Date</td><td class="fill"></td></tr>
      <tr><td>From</td><td class="fill"></td><td>Ref</td><td class="fill"></td></tr>
      <tr><td>Phone</td><td class="fill"></td><td>Fax</td><td class="fill"></td></tr>
      <tr><td>Subject</td><td class="fill"></td><td>Pages</td><td class="fill"></td></tr>
    </table>
    <div class="faint-mark" style="left:42px;top:110px;width:120px;height:120px"></div>
    <svg class="wave" viewBox="0 0 204 30" height="30" preserveAspectRatio="none"><path d="M0 14 Q100 -2 204 12 V30 H0Z" fill="var(--green)"/><path d="M0 16 Q100 0 204 14" stroke="var(--blue)" stroke-width="2" fill="none"/></svg>
  </article>
  <div class="label" style="left:391px;top:346px;width:204px">Fax Form Page</div>

  <article class="piece" style="left:619px;top:89px;width:281px;height:128px">
    <svg style="position:absolute;inset:0" viewBox="0 0 281 128" width="281" height="128"><path d="M0 0 L140 64 L281 0" stroke="#d6dde2" fill="none"/><path d="M0 128 L110 56 M281 128 L170 56" stroke="#e3e8ec" fill="none"/></svg>
    <div class="brand" style="position:absolute;left:100px;top:52px;font-size:6px;background:#fff;padding:2px"><span class="dot" style="width:8px;height:8px"></span>Larkspur Medical Group</div>
  </article>
  <div class="label" style="left:619px;top:221px;width:281px">DL Envelope</div>

  <article class="piece" style="left:619px;top:235px;width:281px;height:120px">
    <div class="brand" style="position:absolute;left:12px;top:14px;font-size:8px"><span class="dot" style="width:14px;height:14px"></span>Larkspur Medical Group</div>
    <div class="card-info" style="left:160px;top:14px">14 S Pebblecroft Ln Fernhollow OR 97390<br>Phone: 847-555-0182<br>www.larkspurmedical.example</div>
    <svg class="wave" viewBox="0 0 281 40" height="40" preserveAspectRatio="none"><path d="M0 20 Q140 -4 281 16 V40 H0Z" fill="var(--green)"/><path d="M0 22 Q140 -2 281 18" stroke="var(--blue)" stroke-width="2" fill="none"/></svg>
  </article>

  <article class="piece" style="left:955px;top:60px;width:221px;height:72px">
    <div class="brand" style="position:absolute;left:8px;top:28px;font-size:7px"><span class="dot" style="width:13px;height:13px"></span>Larkspur Medical Group</div>
    <div class="side-panel"></div>
    <div class="card-info on-green" style="left:124px;top:14px"><strong>Teresa Okonkwo</strong>Phone: 847-555-0182<br>teresa@larkspurmedical.example<br>www.larkspurmedical.example</div>
  </article>
  <div class="label" style="left:955px;top:134px;width:221px">Card Option One</div>

  <article class="piece" style="left:955px;top:149px;width:221px;height:62px">
    <div class="brand" style="position:absolute;left:8px;top:24px;font-size:7px"><span class="dot" style="width:13px;height:13px"></span>Larkspur Medical Group</div>
    <div class="side-panel"></div>
    <div class="card-info on-green" style="left:124px;top:12px">Registered Office:<br>14 S Pebblecroft Ln Fernhollow OR 97390<br>Phone: 847-555-0182</div>
  </article>
  <div class="label" style="left:955px;top:213px;width:221px">Card Option Two</div>

  <article class="piece" style="left:955px;top:221px;width:221px;height:67px">
    <div class="brand" style="position:absolute;left:8px;top:26px;font-size:7px"><span class="dot" style="width:13px;height:13px"></span>Larkspur Medical Group</div>
    <div class="side-panel"></div>
    <div class="card-info on-green" style="left:124px;top:14px">WareHouse Address:<br>2417 Bellhaven Street Fernhollow OR 97391<br>Phone: 847-555-0147</div>
  </article>
  <div class="label" style="left:955px;top:290px;width:221px">Card Option Three</div>

</main>
</body>
</html>
```